Educational Agency in Abu Dhabi looking for an 8 pages website

We are looking for an 8 pages design for a website, we already have one but we need to refine it and it is www.korvalendi.ae - Please base it on logo colours (attached) I have uploaded our logo, website content logo colors to use it for the scheme.
We are looking for a smooth look and content added if possible, I also attached content and logo

Industry/Entity Type

Education

Coding

Coded - Design and coding required

Number of Pages Required

5+ page

```html
<!DOCTYPE html>
<html lang="en">
<head>
<meta charset="utf-8">
<title>Why Study Abroad – Korvalendi</title>
<link href="https://fonts.googleapis.com/css2?family=Poppins:wght@400;500;600&family=Roboto+Condensed:wght@400;700&family=Roboto:wght@400;500;700&display=swap" rel="stylesheet">
<style>
:root{
  --navy:#1b2667;
  --nav:#22307c;
  --nav-active:#141c4d;
  --ink:#222;
  --body:#444;
  --white:#fff;
  --footer:#1a245f;
  --line:#c9cde0;
}
*{box-sizing:border-box;margin:0;padding:0}
html,body{width:1200px;height:3120px;overflow:hidden}
body{position:relative;background:var(--white);font-family:'Poppins',sans-serif;color:var(--ink)}
.site-header{position:absolute;top:0;left:0;width:1200px;height:172px}
.brand{position:absolute;left:124px;top:46px;display:flex;align-items:center;gap:10px;font-family:'Poppins',sans-serif;font-weight:600;font-size:30px;color:var(--navy)}
.brand-dot{width:22px;height:22px;border-radius:50%;background:var(--navy)}
.call{position:absolute;left:448px;top:30px;display:flex;gap:14px;align-items:flex-start}
.call-label{font-family:'Roboto',sans-serif;font-size:19px;color:#222;line-height:22px}
.call-number{font-family:'Roboto',sans-serif;font-size:27px;font-weight:500;color:var(--navy);line-height:32px}
.btn{position:absolute;top:40px;height:40px;border-radius:20px;display:flex;align-items:center;justify-content:center;gap:8px;font-family:'Roboto Condensed',sans-serif;font-size:17px}
.btn-outline{left:731px;width:122px;border:2px solid var(--navy);color:var(--navy)}
.btn-solid{left:869px;width:186px;background:var(--navy);color:var(--white)}
.main-nav{position:absolute;left:256px;top:115px;width:944px;height:57px;background:var(--nav);clip-path:polygon(22px 0,100% 0,100% 100%,0 100%)}
.main-nav ul{list-style:none;display:flex;height:100%;padding-left:24px}
.main-nav li{display:flex;align-items:center;padding:0 11px;font-family:'Roboto Condensed',sans-serif;font-size:17px;color:var(--white)}
.main-nav li.active{background:var(--nav-active)}
.hero{position:absolute;top:172px;left:0;width:1200px;height:298px;background:linear-gradient(90deg,#8a6a55 0%,#6d5a50 35%,#3a3a40 65%,#26283a 100%)}
.hero h1{position:absolute;left:768px;top:128px;font-family:'Roboto Condensed',sans-serif;font-weight:700;font-size:40px;color:var(--white);letter-spacing:-.5px}
.benefits{position:absolute;top:562px;left:144px;width:912px;display:grid;grid-template-columns:441px 441px;column-gap:30px;grid-template-rows:503px 512px 466px auto}
.benefit{text-align:center}
.benefit-photo{width:441px;height:220px;box-shadow:0 3px 8px rgba(0,0,0,.25)}
.benefit h2{font-size:19px;font-weight:500;color:#1b1b1b;margin:30px 0 16px;line-height:28px}
.benefit p{font-size:13.5px;line-height:27px;color:var(--body);padding:0 28px}
.site-footer{position:absolute;top:2527px;left:0;width:1200px;height:593px}
.footer-wave{position:absolute;top:0;left:0}
.footer-body{position:absolute;top:60px;left:0;width:1200px;height:533px;background:var(--footer)}
.footer-col{position:absolute;top:2650px}
.footer-col h3{font-family:'Roboto',sans-serif;font-weight:500;font-size:23px;color:var(--white);text-transform:uppercase}
.footer-col h3 span{text-transform:none;font-weight:400}
.footer-col h3::after{content:"";display:block;width:60px;height:2px;background:var(--white);margin-top:26px}
.quick-links{left:132px}
.quick-links ul{list-style:none;margin-top:30px}
.quick-links li{font-family:'Roboto',sans-serif;font-size:15px;color:var(--white);line-height:24px}
.contact{left:430px}
.contact-item{display:flex;gap:16px;margin-top:28px;font-family:'Roboto',sans-serif;font-size:14.5px;line-height:21px;color:var(--white)}
.contact-item:first-of-type{margin-top:30px}
.icon-ring{flex:0 0 30px;height:30px;border:1.5px solid var(--white);border-radius:50%;display:flex;align-items:center;justify-content:center}
.socials{display:flex;gap:12px;margin-top:24px;padding-left:2px}
.socials span{width:32px;height:32px;border:1.5px solid var(--white);border-radius:50%}
.email-form{left:755px}
.email-form form{margin-top:30px;width:306px}
.field{height:30px;border:1.5px solid var(--line);margin-bottom:13px;padding:5px 10px;font-family:'Roboto',sans-serif;font-size:11px;color:var(--white)}
.field.message{height:64px}
.submit{margin-left:129px;width:177px;height:34px;background:var(--white);color:var(--navy);font-family:'Roboto',sans-serif;font-weight:700;font-size:14px;display:flex;align-items:center;justify-content:center}
.footer-rule{position:absolute;top:2990px;left:132px;width:928px;height:1px;background:rgba(255,255,255,.25)}
.copyright{position:absolute;top:3080px;left:0;width:1200px;text-align:center;font-family:'Roboto',sans-serif;font-size:14px;color:var(--white)}
</style>
</head>
<body>
<header class="site-header">
  <div class="brand"><span class="brand-dot"></span>Korvalendi</div>
  <div class="call">
    <svg width="34" height="34" viewBox="0 0 24 24"><path fill="#555" d="M6.6 10.8a15.2 15.2 0 0 0 6.6 6.6l2.2-2.2a1 1 0 0 1 1-.25 11.4 11.4 0 0 0 3.6.57 1 1 0 0 1 1 1V20a1 1 0 0 1-1 1A17 17 0 0 1 3 4a1 1 0 0 1 1-1h3.5a1 1 0 0 1 1 1c0 1.25.2 2.45.57 3.57a1 1 0 0 1-.25 1z"/></svg>
    <div><div class="call-label">Call Us Today:</div><div class="call-number">+971 2 418 30 72</div></div>
  </div>
  <div class="btn btn-outline"><svg width="16" height="16" viewBox="0 0 24 24" fill="none" stroke="currentColor" stroke-width="2"><path d="M4 20h4L19 9l-4-4L4 16z"/></svg>Apply Now</div>
  <div class="btn btn-solid"><svg width="14" height="16" viewBox="0 0 20 24" fill="none" stroke="currentColor" stroke-width="2"><path d="M2 2h11l5 5v15H2z M6 12h8 M6 16h8"/></svg>Make an Application</div>
  <nav class="main-nav"><ul>
    <li>Home</li><li>About</li><li>Services</li><li class="active">Why Study Abroad</li><li>Study Destination</li><li>English &amp; Other Languages</li><li>Study Online</li><li>Contact</li>
  </ul></nav>
</header>

<section class="hero" role="img" aria-label="Smiling student with glasses in a campus setting"><h1>WHY STUDY ABROAD</h1></section>

<main class="benefits">
  <article class="benefit"><div class="benefit-photo" role="img" aria-label="Student holding a globe" style="background:linear-gradient(135deg,#e6e2dc,#c88a5a 55%,#8c5a3e)"></div>
    <h2>International Exposure</h2>
    <p>Studying while living in a foreign country will give you a chance to interact with students and professors in a fully immersed environment. As a result, communication, personality and self confidence will advance by leaps and bounds.</p></article>
  <article class="benefit"><div class="benefit-photo" role="img" aria-label="Students writing in an exam hall" style="background:linear-gradient(135deg,#2d4a7a,#7d8ea8 50%,#d7c9a8)"></div>
    <h2>Variety of Courses and Specializations</h2>
    <p>A diverse conglomeration of specialized training is available. To name a few starting from Automotive Design, Nano Technology, Robotics, Game Design, Mining, Geospatial Science, VLSI, Wireless communications, Radar/Satellite Communications, as well as Highway/Transportation. The possibilities are endless!</p></article>
  <article class="benefit"><div class="benefit-photo" role="img" aria-label="Lecturer addressing students in a lecture hall" style="background:linear-gradient(135deg,#c9a04a,#b07d5a 50%,#4a4038)"></div>
    <h2>Quality infrastructure and Facilities</h2>
    <p>Most of the Universities abroad have excellent profession career centers with qualified counselors to provide career advice. They will assist in guiding where to apply for jobs after completing courses studies. The career centers also have established frameworks to guide you in applying and interviewing for that targeted job.</p></article>
  <article class="benefit"><div class="benefit-photo" role="img" aria-label="Job candidates waiting for an interview" style="background:linear-gradient(135deg,#d8d6d2,#8a8c92 50%,#3a3c44)"></div>
    <h2>Job Opportunities</h2>
    <p>Those who study and work abroad are more likely to be sought after in their home country for high level positions upon their return. The majority of the MNCs see internationally educated students as preferable qualified candidates</p></article>
  <article class="benefit"><div class="benefit-photo" role="img" aria-label="Students working together at computers" style="background:linear-gradient(135deg,#c8ccd2,#6a6e78 50%,#8a5a40)"></div>
    <h2>Immigration Permanent<br>Residency / Citizenship Options</h2>
    <p>University graduates are the most eligible immigrants to obtain permanent residency opportunities<br>in any country.</p></article>
  <article class="benefit"><div class="benefit-photo" role="img" aria-label="Books, flags and a note about learning a new language" style="background:linear-gradient(135deg,#6a7a3a,#c8a070 45%,#b8323a)"></div>
    <h2>Developing Language Skills</h2>
    <p>International Universities offer language programs and encourage students to advance in Spanish, French, and English in an effort to equip students with a balanced degree that makes them appealing to the world market.</p></article>
  <article class="benefit"><div class="benefit-photo" role="img" aria-label="Student with a laptop in a park" style="background:linear-gradient(135deg,#5a8a3a,#3a5a9a 50%,#c8b070)"></div>
    <h2>Overall personality development</h2>
    <p>Confidence in networking happens outside of the classroom. Students are exposed to extracurricular opportunities and sporting activities which lead to building long lasting friendly connections.</p></article>
  <article class="benefit"><div class="benefit-photo" role="img" aria-label="Hands typing on a laptop at a wooden table" style="background:linear-gradient(135deg,#d8904a,#a86a3a 50%,#7a6a8a)"></div>
    <h2>An investment with returns</h2>
    <p>Education is not a wasted investment. There are jobs and internships available that will allow you to maximize the value of the time and money exerted. Visa extension options are also available.</p></article>
</main>

<footer class="site-footer">
  <svg class="footer-wave" width="1200" height="80" viewBox="0 0 1200 80">
    <path d="M0 40 C300 70 700 78 1200 6 L1200 80 L0 80Z" fill="#1a245f"/>
    <path d="M0 42 C350 66 760 70 1200 0" fill="none" stroke="#1a245f" stroke-width="6"/>
  </svg>
  <div class="footer-body"></div>
</footer>

<div class="footer-col quick-links"><h3>Quick Links</h3>
  <ul><li>Home</li><li>About Us</li><li>Services</li><li>Why Study Abroad</li><li>Study Destination</li><li>English And Other Languages</li><li>Study Online</li><li>Apply</li><li>Contact Us</li></ul>
</div>
<div class="footer-col contact"><h3>Contact <span>US</span></h3>
  <div class="contact-item"><span class="icon-ring"><svg width="12" height="14" viewBox="0 0 24 28"><path fill="#fff" d="M12 0a10 10 0 0 0-10 10c0 7 10 18 10 18s10-11 10-18A10 10 0 0 0 12 0zm0 14a4 4 0 1 1 0-8 4 4 0 0 1 0 8z"/></svg></span>
    <div>Harbour View Complex<br>Al Nahda Tower, Suite – 14<br>2nd Floor, PO Box – 4127</div></div>
  <div class="contact-item"><span class="icon-ring"><svg width="14" height="14" viewBox="0 0 24 24"><path fill="#fff" d="M6.6 10.8a15.2 15.2 0 0 0 6.6 6.6l2.2-2.2a1 1 0 0 1 1-.25 11.4 11.4 0 0 0 3.6.57 1 1 0 0 1 1 1V20a1 1 0 0 1-1 1A17 17 0 0 1 3 4a1 1 0 0 1 1-1h3.5a1 1 0 0 1 1 1c0 1.25.2 2.45.57 3.57a1 1 0 0 1-.25 1z"/></svg></span>
    <div>Phone: +971 2 418 30 72<br>Mobile: 971 52 734 2086<br>+971 503917264, +971 50 285 6140</div></div>
  <div class="contact-item"><span class="icon-ring"><svg width="14" height="11" viewBox="0 0 24 18" fill="none" stroke="#fff" stroke-width="2"><rect x="1" y="1" width="22" height="16"/><path d="M1 1l11 9 11-9"/></svg></span>
    <div style="padding-top:4px">E - Mail : info@korvalendi.ae</div></div>
  <div class="socials"><span></span><span></span><span></span></div>
</div>
<div class="footer-col email-form"><h3>Email <span>US</span></h3>
  <form>
    <div class="field">First Name</div>
    <div class="field">Email Address</div>
    <div class="field">Phone Number</div>
    <div class="field message">Message</div>
    <div class="submit">SUBMIT</div>
  </form>
</div>
<div class="footer-rule"></div>
<p class="copyright">© Copyright 2018 Korvalendi. All Rights Reserved.</p>
</body>
</html>
```